Cyber Security Consultancy needs website design.

We need a website design for a cyber security startup in Dubai.

Coding

Coded - Design and coding required

Number of Pages Required

1 page

Colors
0054AA
0677BA
7BADD7
CADEEF
E8F1F8

```html
<!DOCTYPE html>
<html lang="en">
<head>
<meta charset="utf-8">
<title>Harbor Shield — Cyber Security Consultancy</title>
<link href="https://fonts.googleapis.com/css2?family=Roboto:wght@300;400;500;700&family=Rubik:wght@300;600&display=swap" rel="stylesheet">
<style>
:root{
  --blue-deep:#0054AA;
  --blue:#0677BA;
  --blue-bright:#1E88D8;
  --blue-soft:#7BADD7;
  --blue-pale:#CADEEF;
  --blue-mist:#E8F1F8;
  --black:#000;
  --ink:#222;
  --muted:#8a8a8a;
  --white:#fff;
  --line:#2a2a2a;
}
*{box-sizing:border-box;margin:0;padding:0}
html,body{width:1200px;height:3216px;overflow:hidden}
body{font-family:"Roboto",sans-serif;color:var(--ink);background:var(--white);position:relative}
a{color:inherit;text-decoration:none}
.section{position:absolute;left:0;width:1200px}

/* Hero */
.hero{top:0;height:680px;background:var(--black);overflow:hidden}
.hero-art{position:absolute;inset:0;background:
  radial-gradient(circle at 830px 330px,#2f8fe0 0,#0d4f9a 130px,#062a5c 260px,rgba(2,14,36,0) 430px),
  radial-gradient(ellipse at 1050px 560px,#0a3c7a 0,rgba(0,0,0,0) 300px),
  linear-gradient(90deg,#000 0,#010610 40%,#021a3d 100%)}
.brand{position:absolute;display:flex;align-items:center;gap:12px;font-weight:700;color:var(--white);letter-spacing:.5px}
.brand-mark{background:var(--blue);display:block}
.hero .brand{left:110px;top:44px;font-size:22px}
.hero .brand-mark{width:26px;height:26px}
.contact-bar{position:absolute;right:116px;top:32px;display:flex;gap:40px;font-size:15px;color:var(--white)}
.contact-bar span{display:flex;align-items:center;gap:12px}
.contact-bar .phone{color:var(--blue-bright)}
.nav{position:absolute;right:116px;top:74px;display:flex;align-items:center;gap:30px;font-size:13px;font-weight:700;color:var(--white)}
.nav .active{color:var(--blue-bright)}
.nav .quote{background:var(--blue);padding:9px 14px;border:1px solid var(--blue-bright)}
.hero-copy{position:absolute;left:115px;top:222px;width:420px;color:var(--white)}
.eyebrow{font-family:"Rubik",sans-serif;font-weight:300;font-size:27px}
.hero-title{font-family:"Rubik",sans-serif;font-weight:600;font-size:42px;line-height:56px;color:var(--blue-bright);margin-top:6px}
.hero-text{font-size:14px;line-height:22px;margin-top:14px}
.btn-outline{display:inline-block;margin-top:26px;background:var(--blue);border:1px solid var(--blue-pale);color:var(--white);font-size:13px;padding:11px 30px}
.dots{position:absolute;left:556px;top:626px;display:flex;gap:10px}
.dots i{width:14px;height:14px;border-radius:50%;border:2px solid var(--white)}
.dots i.on{background:var(--blue-bright);border-color:var(--blue-soft)}

/* Shared headings */
.section-title{font-family:"Roboto",sans-serif;font-weight:700;font-size:36px;text-align:center;color:var(--ink)}
.section-title em{font-style:normal;color:var(--blue)}
.rule{width:62px;height:3px;background:var(--blue);margin:14px auto 0}
.section-lead{text-align:center;font-size:15px;color:#555;margin-top:18px}
.read-more{display:inline-flex;align-items:center;gap:12px;font-size:12px;text-decoration:underline;color:#333}
.read-more i{width:22px;height:22px;border-radius:50%;background:#222;display:grid;place-items:center}
.read-more.hl{color:var(--blue)}
.read-more.hl i{background:var(--blue)}

/* Services */
.services{top:680px;height:778px;padding-top:66px}
.service-grid{position:absolute;left:110px;top:178px;display:grid;grid-template-columns:repeat(3,298px);column-gap:42px}
.service-photo{height:282px;border-radius:8px}
.service-card{text-align:center}
.service-card h3{font-weight:500;font-size:19px;line-height:25px;margin-top:42px;color:var(--ink)}
.service-card.featured h3{color:var(--blue)}
.service-card p{font-size:12px;line-height:22px;color:var(--muted);margin:12px 20px 14px}
.ph-infra{background:linear-gradient(160deg,#0b4a66,#0a1e2c 55%,#03090f)}
.ph-app{background:linear-gradient(160deg,#3b2a72,#d14b9a 45%,#1c6ab5 80%,#081632)}
.ph-red{background:linear-gradient(180deg,#2a0509,#5e0d17 50%,#0b0204)}

/* About */
.about{top:1458px;height:592px;overflow:hidden}
.about-art{position:absolute;inset:0;background:
  radial-gradient(circle at 860px 260px,#0f6fd0 0,#0a3f86 170px,rgba(4,22,52,0) 320px),
  radial-gradient(ellipse at 340px 470px,#1b6a78 0,rgba(4,25,48,0) 340px),
  linear-gradient(135deg,#03152c,#041d3c 60%,#020c1c)}
.about-copy{position:absolute;left:112px;top:100px;width:470px;color:var(--white)}
.about-copy h2{font-size:36px;font-weight:700}
.about-copy h2 em{font-style:normal;color:var(--blue-bright)}
.about-copy .rule{margin:10px 0 0}
.about-lead{font-weight:700;font-size:15px;line-height:24px;margin-top:18px}
.about-copy p.body{font-size:12px;line-height:22px;margin-top:14px;color:#e6eef8}
.btn-solid{display:inline-block;margin-top:24px;background:var(--blue);color:var(--white);font-size:12px;font-weight:700;padding:11px 20px;border-radius:3px}

/* News */
.news{top:2050px;height:636px;padding-top:86px}
.news-grid{position:absolute;left:110px;top:184px;display:grid;grid-template-columns:repeat(4,232px);column-gap:18px}
.news-photo{height:190px}
.news-card h3{font-weight:400;font-size:15px;line-height:25px;margin-top:10px;color:var(--ink)}
.news-card .read-more{margin-top:8px;font-size:12px}
.ph-n1{background:linear-gradient(140deg,#6fa9d6,#174d86 60%,#08223d)}
.ph-n2{background:radial-gradient(circle at 55% 50%,#2a9be6,#0a4d8f 60%,#052647)}
.ph-n3{background:linear-gradient(140deg,#0d2034,#2d5877 50%,#0b1622)}
.ph-n4{background:linear-gradient(140deg,#1a2a3a,#5a6f86 50%,#131c26)}
.btn-view{position:absolute;left:536px;top:516px;width:126px;height:36px;background:var(--blue-deep);color:var(--white);font-size:12px;font-weight:700;display:grid;place-items:center;border-radius:3px;box-shadow:0 3px 6px rgba(0,0,0,.3)}

/* Footer */
.footer{top:2686px;height:530px;background:var(--black);color:var(--white)}
.footer .brand{left:110px;top:50px;font-size:44px;gap:20px}
.footer .brand-mark{width:52px;height:52px}
.socials{position:absolute;right:116px;top:86px;display:flex;gap:16px}
.socials i{width:17px;height:17px;border-radius:50%;background:var(--white)}
.socials i:first-child{background:var(--blue)}
.footer-cols{position:absolute;left:110px;top:172px;display:grid;grid-template-columns:382px 308px 290px}
.footer-col{border-left:1px solid var(--line);padding:0 0 0 26px;height:296px;position:relative}
.footer-col::before{content:"";position:absolute;left:-3px;top:40px;width:5px;height:72px;background:#555}
.footer-col h4{font-size:15px;font-weight:500;color:var(--blue-bright);margin-top:90px}
.footer-col ul{list-style:none;margin-top:24px}
.footer-col li{font-size:12px;line-height:27px;display:flex;align-items:center;gap:6px}
.footer-col li::before{content:"";width:10px;height:10px;border:1px solid var(--blue-bright);border-radius:50%}
.reach p{font-size:12px;line-height:28px;display:flex;gap:6px;align-items:flex-start}
.reach .gap{margin-top:40px}
.subscribe p{font-size:12px;line-height:28px;margin-top:12px;width:200px}
.sub-form{display:flex;margin-top:16px;width:262px;height:48px;border:1px solid var(--blue)}
.sub-form span{flex:1;font-size:11px;color:#bbb;padding:16px 24px}
.sub-form b{width:66px;background:var(--blue);display:grid;place-items:center}
.copyright{position:absolute;left:0;width:1200px;top:498px;text-align:center;font-size:11px;color:#aaa}
</style>
</head>
<body>

<header class="section hero">
  <div class="hero-art" role="img" aria-label="Open hand beneath a glowing padlock ringed by security and cloud icons on a dark blue background"></div>
  <div class="brand"><span class="brand-mark"></span>HARBOR SHIELD</div>
  <div class="contact-bar">
    <span class="phone"><svg width="20" height="20" viewBox="0 0 24 24" fill="#1E88D8"><path d="M6.6 10.8a15 15 0 0 0 6.6 6.6l2.2-2.2a1 1 0 0 1 1-.25 11 11 0 0 0 3.6.6 1 1 0 0 1 1 1V20a1 1 0 0 1-1 1A17 17 0 0 1 3 4a1 1 0 0 1 1-1h3.5a1 1 0 0 1 1 1c0 1.25.2 2.45.6 3.6a1 1 0 0 1-.25 1z"/></svg>+1 555 010 0199</span>
    <span><svg width="26" height="20" viewBox="0 0 26 20"><rect x="1" y="1" width="24" height="18" fill="#fff"/><path d="M1 1l12 10 12-10" stroke="#000" stroke-width="2" fill="none"/></svg>info@harborshield.net</span>
  </div>
  <nav class="nav">
    <a class="active">HOME</a><a>ABOUT US</a><a>SERVICES</a><a>CONTACT</a><a class="quote">GET A QUOTE</a>
  </nav>
  <div class="hero-copy">
    <p class="eyebrow">Harbor Shield</p>
    <h1 class="hero-title">Cyber Security<br>Consultancy</h1>
    <p class="hero-text">Lorem Ipsum is simply dummy text of the printing and typesetting industry. Lorem Ipsum has been the industry's standard dummy text ever since the 1500s.</p>
    <a class="btn-outline">Get started</a>
  </div>
  <div class="dots"><i class="on"></i><i></i><i></i><i></i></div>
</header>

<section class="section services">
  <h2 class="section-title">Our <em>Services</em></h2>
  <div class="rule"></div>
  <p class="section-lead">Neque porro quisquam est qui dolorem ipsum quia dolor sit amet, consectetur, adipisci velit...</p>
  <div class="service-grid">
    <article class="service-card">
      <div class="service-photo ph-infra" role="img" aria-label="Analyst in a hood facing monitors with network maps"></div>
      <h3>Infrastructure<br>Penetration Testing</h3>
      <p>Sed ut perspiciatis unde omnis iste natus error sit voluptatem accusantium doloremque laudantium, totam rem aperiam, eaque ipsa quae ab illo inventore veritatis</p>
      <a class="read-more"><i><svg width="10" height="10" viewBox="0 0 10 10"><path d="M3 1l4 4-4 4" stroke="#fff" stroke-width="2" fill="none"/></svg></i>Read More &gt;</a>
    </article>
    <article class="service-card featured">
      <div class="service-photo ph-app" role="img" aria-label="Colourful rack of glowing application blocks"></div>
      <h3>Application<br>Penetration Testing</h3>
      <p>Sed ut perspiciatis unde omnis iste natus error sit voluptatem accusantium doloremque laudantium, totam rem aperiam, eaque ipsa quae ab illo inventore veritatis</p>
      <a class="read-more hl"><i><svg width="10" height="10" viewBox="0 0 10 10"><path d="M3 1l4 4-4 4" stroke="#fff" stroke-width="2" fill="none"/></svg></i>Read More &gt;</a>
    </article>
    <article class="service-card">
      <div class="service-photo ph-red" role="img" aria-label="Rows of hooded figures at laptops under red light"></div>
      <h3>Red Teaming</h3>
      <p>Sed ut perspiciatis unde omnis iste natus error sit voluptatem accusantium doloremque laudantium, totam rem aperiam, eaque ipsa quae ab illo inventore veritatis</p>
      <a class="read-more"><i><svg width="10" height="10" viewBox="0 0 10 10"><path d="M3 1l4 4-4 4" stroke="#fff" stroke-width="2" fill="none"/></svg></i>Read More &gt;</a>
    </article>
  </div>
</section>

<section class="section about">
  <div class="about-art" role="img" aria-label="Consultant at a laptop before a large glowing shield with padlock icons and a network of light points"></div>
  <div class="about-copy">
    <h2>About <em>Harbor Shield</em></h2>
    <div class="rule"></div>
    <p class="about-lead">Neque porro quisquam est qui dolorem ipsum quia dolor sit amet, consectetur, adipisci velit...</p>
    <p class="body">Sed ut perspiciatis unde omnis iste natus error sit voluptatem accusantium doloremque laudantium, totam rem aperiam, eaque ipsa quae ab illo inventore veritatis et quasi architecto beatae vitae dicta sunt explicabo.</p>
    <p class="body">Nemo enim ipsam voluptatem quia voluptas sit aspernatur aut odit aut fugit, sed quia consequuntur magni dolores eos qui ratione voluptatem sequi nesciunt. Neque porro quisquam est, qui dolorem ipsum quia dolor sit amet, consectetur, adipisci velit, sed quia non numquam eius modi tempora incidunt ut labore et dolore magnam aliquam quaerat voluptatem.</p>
    <a class="btn-solid">LEARN MORE ABOUT US</a>
  </div>
</section>

<section class="section news">
  <h2 class="section-title">Our <em>Latest News</em></h2>
  <div class="rule"></div>
  <p class="section-lead">Neque porro quisquam est qui dolorem ipsum quia dolor sit amet, consectetur, adipisci velit...</p>
  <div class="news-grid">
    <article class="news-card"><div class="news-photo ph-n1" role="img" aria-label="Hands typing on a keyboard with data overlay"></div><h3>De Finibus Bonorum et Malorum", written by Cicero in 45 BC</h3><a class="read-more">Read More &gt;</a></article>
    <article class="news-card"><div class="news-photo ph-n2" role="img" aria-label="Glowing blue padlock on a laptop"></div><h3>De Finibus Bonorum et Malorum", written by Cicero in 45 BC</h3><a class="read-more">Read More &gt;</a></article>
    <article class="news-card"><div class="news-photo ph-n3" role="img" aria-label="Two engineers in a server room with a tablet"></div><h3>De Finibus Bonorum et Malorum", written by Cicero in 45 BC</h3><a class="read-more">Read More &gt;</a></article>
    <article class="news-card"><div class="news-photo ph-n4" role="img" aria-label="Team working at computers in a security office"></div><h3>De Finibus Bonorum et Malorum", written by Cicero in 45 BC</h3><a class="read-more">Read More &gt;</a></article>
  </div>
  <a class="btn-view">VIEW MORE</a>
</section>

<footer class="section footer">
  <div class="brand"><span class="brand-mark"></span>HARBOR SHIELD</div>
  <div class="socials"><i></i><i></i><i></i><i></i><i></i></div>
  <div class="footer-cols">
    <div class="footer-col reach">
      <h4>To Reach Us</h4>
      <p style="margin-top:20px"><svg width="10" height="14" viewBox="0 0 10 14" style="margin-top:7px"><path d="M5 0a5 5 0 0 1 5 5c0 4-5 9-5 9S0 9 0 5a5 5 0 0 1 5-5z" fill="#1E88D8"/><circle cx="5" cy="5" r="2" fill="#000"/></svg>418 Cedar Lane, Marlow Bay,<br>California, 93555.</p>
      <p class="gap"><svg width="12" height="12" viewBox="0 0 24 24" fill="#1E88D8" style="margin-top:8px"><path d="M6.6 10.8a15 15 0 0 0 6.6 6.6l2.2-2.2a1 1 0 0 1 1-.25 11 11 0 0 0 3.6.6 1 1 0 0 1 1 1V20a1 1 0 0 1-1 1A17 17 0 0 1 3 4a1 1 0 0 1 1-1h3.5a1 1 0 0 1 1 1c0 1.25.2 2.45.6 3.6a1 1 0 0 1-.25 1z"/></svg>0100 555 0142</p>
      <p class="gap"><svg width="13" height="10" viewBox="0 0 13 10" style="margin-top:9px"><rect x=".5" y=".5" width="12" height="9" fill="none" stroke="#1E88D8"/><path d="M.5.5l6 5 6-5" stroke="#1E88D8" fill="none"/></svg>info@harborshield.net</p>
    </div>
    <div class="footer-col">
      <h4>Quick Links</h4>
      <ul><li>Home</li><li>About Us</li><li>Services</li><li>Project</li><li>Industry News</li><li>Contact</li></ul>
    </div>
    <div class="footer-col subscribe">
      <h4>Subscribe</h4>
      <p>Neque porro quisquam est qui dolorem ipsum quia dolor sit amet,</p>
      <div class="sub-form"><span>Email Address</span><b><svg width="18" height="18" viewBox="0 0 24 24"><path d="M2 12L22 3l-5 18-5-7-10-2z" fill="#fff"/></svg></b></div>
    </div>
  </div>
  <p class="copyright">Harbor Shield © 2024 All Rights Reserved.</p>
</footer>

</body>
</html>
```